KVM TL Academy

Cosmetic dentistry Utilizing the latest smile simulation technology (KVM )to show patients their after smile results and allow them to be involved in the design prior to treatment
Please review the following websites to understand the concept:

http://www.clipvane.example/watch?v=Qw7LmRtZ2kP
http://www.clipvane.example/watch?v=Hb4NcVyUe8s

www.kvmportal.com.au

www.tobiaslangford.com.au
Dr Tobias Langford the Clinical director of The TL Academy is the leading cosmetic dentist in Australia and runs the Institute that teaches dentists how to deliver their cosmetic results
he also owns the Australian rites to KVM

It may be necessary to do 2 versions for the cards

One for the female market that basically trends of the Clipvane site i sent that "sex sells" and youthful smiles are more attractive for the aging woman who has the $$ to spend on a Smile makeover

A second card that is for the male senior manager exec who has not looked after their teeth due to work commitments but does not want the Smile Makeover look yet they need to compete with the younger execs snapping at their heels and if they are in the media they want to have an improved smile

The Simulation process we have developed allows them to see the end result before they commit
Their greatest fear is the obvious smile change and the CHICLET SMILE look

Target Market(s)

25-45 year olds, first group the professional male, second group females who want to improve their smile but be able to control the result

Industry/Entity Type

Clipvane

Contact Information for Business Card

Kinetic Visage Method
The TL Academy

Requirements
Must have
• The KVM logo on front with The TL Academy
Nice to have
• background picture of beautiful smile right hand side with copy over it
KVM logo left hand side

```html
<!DOCTYPE html>
<html lang="en">
<head>
<meta charset="utf-8">
<title>KVM TL Academy – Business Card</title>
<link rel="stylesheet" href="https://fonts.googleapis.com/css2?family=Source+Sans+3:wght@300;400&display=swap">
<style>
  :root {
    --page-bg: #e9e7e4;
    --panel-dark: #262b2e;
    --band-grey: #7b7c7d;
    --text-grey: #8d9194;
    --text-light: #c9cccd;
    --accent-red: #e8452c;
    --card-white: #ffffff;
    --photo-warm: #d9a58a;
    --photo-deep: #6b4637;
  }
  * { margin: 0; padding: 0; box-sizing: border-box; }
  html, body {
    width: 1200px;
    height: 1000px;
    overflow: hidden;
    background: var(--page-bg);
    font-family: "Source Sans 3", "Myriad Pro", Arial, sans-serif;
  }
  .business-card {
    position: absolute;
    left: 100px;
    top: 214px;
    width: 1000px;
    height: 571px;
    border-radius: 40px;
    overflow: hidden;
    background: var(--card-white);
    box-shadow: 0 10px 30px rgba(0,0,0,0.25);
  }
  .card-shapes {
    position: absolute;
    inset: 0;
    width: 1000px;
    height: 571px;
  }
  .card-content {
    position: absolute;
    left: 78px;
    top: 40px;
    width: 420px;
  }
  .brand-mark {
    width: 130px;
    height: 130px;
    border: 2px solid var(--band-grey);
    border-radius: 50%;
    margin-left: 40px;
  }
  .brand-name {
    margin-top: 18px;
    font-size: 62px;
    font-weight: 400;
    line-height: 1;
    letter-spacing: 4px;
    color: var(--accent-red);
  }
  .brand-tagline {
    margin-top: 4px;
    font-size: 15px;
    font-weight: 400;
    color: var(--text-grey);
  }
  .academy-name {
    margin-top: 14px;
    font-size: 38px;
    font-weight: 400;
    color: var(--text-grey);
  }
  .address-label {
    margin-top: 16px;
    font-size: 24px;
    color: var(--accent-red);
  }
  .address-lines {
    font-size: 23px;
    font-weight: 300;
    line-height: 1.32;
    color: var(--text-light);
  }
  .phone-line {
    display: flex;
    align-items: center;
    gap: 6px;
    font-size: 23px;
    font-weight: 300;
    color: var(--text-light);
  }
  .phone-icon { width: 12px; height: 20px; }
</style>
</head>
<body>
  <section class="business-card">
    <svg class="card-shapes" viewBox="0 0 1000 571" xmlns="http://www.w3.org/2000/svg">
      <defs>
        <radialGradient id="smileTone" cx="0.62" cy="0.55" r="0.55">
          <stop offset="0" stop-color="var(--photo-warm)"/>
          <stop offset="0.55" stop-color="#c99179"/>
          <stop offset="0.8" stop-color="var(--photo-deep)" stop-opacity="0.35"/>
          <stop offset="1" stop-color="#ffffff" stop-opacity="0"/>
        </radialGradient>
      </defs>
      <rect class="smile-photo" x="520" y="0" width="480" height="571" fill="url(#smileTone)"
            role="img" aria-label="Photograph of a smiling young woman resting her face in her hands"/>
      <path class="grey-band" d="M0 0 H568 C612 190 540 430 330 571 H0 Z" fill="var(--band-grey)"/>
      <path class="dark-panel" d="M0 0 H528 C570 190 500 430 292 571 H0 Z" fill="var(--panel-dark)"/>
    </svg>

    <div class="card-content">
      <div class="brand-mark"></div>
      <div class="brand-name">KVM</div>
      <div class="brand-tagline">Kinetic Visage Method</div>
      <div class="academy-name">TL Academy</div>
      <div class="address-label">Address</div>
      <div class="address-lines">
        <div>Level 1</div>
        <div>418 Harlow</div>
        <div>St. Carrington 3090 Australia</div>
      </div>
      <div class="phone-line">
        <svg class="phone-icon" viewBox="0 0 12 20" xmlns="http://www.w3.org/2000/svg">
          <rect x="1" y="1" width="10" height="18" rx="2" fill="none" stroke="var(--accent-red)" stroke-width="2"/>
          <rect x="4" y="15" width="4" height="2" fill="var(--accent-red)"/>
        </svg>
        <span>1800 527419</span>
      </div>
    </div>
  </section>
</body>
</html>
```